Mobile App UI Redesign for Service Booking app

Bookora is a business management system made especially for service based businesses (our subscribers). It enables systemising your service businesses. This can be used by diverse industries like automotive service, beauty (hair salons, nail spas), Spas, Chiropractor, acupuntcure, osteo, yoga studio, business coach, etc.

One component of this management system is a consumer app that the users (customers of our subscribers) can use to book in services with businesses (subscribers). Any business that provides services, either 1-to-1(personal training/ hair cut, etc) or 1-to-many (classes/ sessions)can get their users to download the app and book straight away in real time.

The current app is built as a version that is available to all subscribers. Hence the search screen at the beginning of the app. Our subscribers have the option to brand this app, with their own logo and colours.

The UI of the app needs to be designed using flat and clean UI design trends that are currently prevailing for B2C apps. Even the sliding menu panel can be removed and alternative placement of this functionality can be suggested. The color palette used for the design should be limited (3-5 colours) so that minimum effort is required to convert this into our customers branded app.

The Current UI screens are open to suggestions for change. For ease of booking in minimum steps, consolidation of functionality on different screens can be suggested, accompanies by a rational reason with the objective of having a simple and straight forward user experience.

User should be able to move from one function to another (booking > view appointments > profile) in no more than 1 or max 2 gestures.

Target Market(s)

Service Based Businesses that require customers to book in services or sessions with them. These can include health services (chiro, physio, osteo, accupuncture, etc) Beauty (hair salon, nail spa, health spa, etc) automotive service (car service, motorcycle service, bike service, etc)

Industry/Entity Type

Business

Requirements
Must have
• Design files to be delivered in JPG and Vectored PSD format

```html
<!DOCTYPE html>
<html lang="en">
<head>
<meta charset="utf-8">
<title>Bookora – Services</title>
<link href="https://fonts.googleapis.com/css2?family=Roboto:wght@400;500;700&display=swap" rel="stylesheet">
<style>
  :root {
    --brand: #38ace4;
    --brand-light: #e3f3fc;
    --white: #ffffff;
    --text-title: #5a5f66;
    --text-meta: #3c4046;
    --divider: #e4e7ea;
    --canvas: #ffffff;
  }
  * { box-sizing: border-box; margin: 0; padding: 0; }
  html, body {
    width: 1200px; height: 2352px; overflow: hidden;
    background: var(--canvas);
    font-family: "Roboto", Arial, sans-serif;
  }
  .app { width: 1200px; height: 2352px; display: flex; flex-direction: column; }

  .app-header { background: var(--brand); color: var(--white); }
  .status-bar {
    height: 64px; display: flex; align-items: center; justify-content: space-between;
    padding: 0 28px; font-size: 30px; font-weight: 500;
  }
  .status-bar .carrier, .status-bar .system { display: flex; align-items: center; gap: 14px; }
  .signal { display: flex; gap: 5px; }
  .signal span { width: 12px; height: 12px; border-radius: 50%; background: var(--white); }
  .signal span.off { background: transparent; border: 2px solid var(--white); }
  .battery { width: 56px; height: 26px; border: 3px solid var(--white); border-radius: 5px; padding: 3px; position: relative; }
  .battery::after { content: ""; position: absolute; right: -8px; top: 6px; width: 4px; height: 9px; background: var(--white); }
  .battery i { display: block; width: 100%; height: 100%; background: var(--white); }

  .nav-bar {
    height: 120px; display: flex; align-items: center; justify-content: space-between; padding: 0 36px;
  }
  .nav-title { font-size: 52px; font-weight: 500; letter-spacing: 1px; }
  .nav-actions { display: flex; align-items: center; gap: 44px; }

  .segment-wrap { padding: 4px 36px 34px; }
  .segment {
    display: flex; height: 90px; border: 3px solid var(--white); border-radius: 8px; overflow: hidden;
  }
  .segment-tab {
    flex: 1; display: flex; align-items: center; justify-content: center;
    font-size: 38px; font-weight: 500;
  }
  .segment-tab.is-active { background: var(--white); color: var(--brand); }

  .service-list { flex: 1; list-style: none; display: flex; flex-direction: column; }
  .service-item {
    flex: 1; display: flex; align-items: center; padding: 0 36px 0 40px; position: relative;
  }
  .service-item + .service-item::before {
    content: ""; position: absolute; top: 0; left: 250px; right: 0; height: 2px; background: var(--divider);
  }
  .service-icon {
    width: 172px; height: 172px; border-radius: 50%;
    border: 4px solid var(--brand); background: var(--brand-light); flex: none;
  }
  .service-info { flex: 1; margin-left: 44px; }
  .service-name { font-size: 40px; color: var(--text-title); font-weight: 400; }
  .service-meta { margin-top: 20px; font-size: 28px; font-weight: 700; color: var(--text-meta); }
  .service-meta .sep { font-weight: 400; margin: 0 16px; color: #9aa0a6; }
  .checkbox { width: 56px; height: 56px; flex: none; }
</style>
</head>
<body>
<div class="app">
  <header class="app-header">
    <div class="status-bar">
      <div class="carrier">
        <div class="signal"><span></span><span></span><span></span><span class="off"></span><span class="off"></span></div>
        <span>Carrier</span>
        <svg width="34" height="26" viewBox="0 0 34 26"><path d="M2 9a21 21 0 0 1 30 0M7 14a14 14 0 0 1 20 0M12 19a7 7 0 0 1 10 0" stroke="#fff" stroke-width="3.5" fill="none" stroke-linecap="round"/><circle cx="17" cy="23" r="2.5" fill="#fff"/></svg>
      </div>
      <span class="time">4:21 PM</span>
      <div class="system">
        <svg width="18" height="30" viewBox="0 0 18 30"><path d="M2 8l14 14-7 6V2l7 6L2 22" stroke="#fff" stroke-width="3" fill="none"/></svg>
        <span>100%</span>
        <div class="battery"><i></i></div>
      </div>
    </div>
    <nav class="nav-bar">
      <svg class="menu-icon" width="52" height="40" viewBox="0 0 52 40"><rect y="2" width="52" height="6" rx="2" fill="#fff"/><rect y="17" width="52" height="6" rx="2" fill="#fff"/><rect y="32" width="52" height="6" rx="2" fill="#fff"/></svg>
      <h1 class="nav-title">Bookora</h1>
      <div class="nav-actions">
        <svg class="grid-icon" width="42" height="42" viewBox="0 0 42 42" fill="#fff"><circle cx="6" cy="6" r="5"/><circle cx="21" cy="6" r="5"/><circle cx="36" cy="6" r="5"/><circle cx="6" cy="21" r="5"/><circle cx="21" cy="21" r="5"/><circle cx="36" cy="21" r="5"/><circle cx="6" cy="36" r="5"/><circle cx="21" cy="36" r="5"/><circle cx="36" cy="36" r="5"/></svg>
        <svg class="next-icon" width="26" height="44" viewBox="0 0 26 44"><path d="M4 4l18 18L4 40" stroke="#fff" stroke-width="5" fill="none" stroke-linecap="round" stroke-linejoin="round"/></svg>
      </div>
    </nav>
    <div class="segment-wrap">
      <div class="segment">
        <div class="segment-tab is-active">Services</div>
        <div class="segment-tab">Classes</div>
      </div>
    </div>
  </header>

  <ul class="service-list">
    <li class="service-item">
      <div class="service-icon" role="img" aria-label="Scissors and comb icon"></div>
      <div class="service-info"><p class="service-name">Hair Cutting</p><p class="service-meta">30 min<span class="sep">|</span>90 $</p></div>
      <svg class="checkbox" viewBox="0 0 56 56"><rect x="4" y="4" width="48" height="48" fill="none" stroke="#38ace4" stroke-width="4"/></svg>
    </li>
    <li class="service-item">
      <div class="service-icon" role="img" aria-label="Updo hairstyle icon"></div>
      <div class="service-info"><p class="service-name">Hair Up Styles</p><p class="service-meta">30 min<span class="sep">|</span>20 $</p></div>
      <svg class="checkbox" viewBox="0 0 56 56"><rect x="4" y="4" width="48" height="48" fill="none" stroke="#38ace4" stroke-width="4"/><path d="M14 28l10 10 24-26" fill="none" stroke="#38ace4" stroke-width="6" stroke-linecap="round" stroke-linejoin="round"/></svg>
    </li>
    <li class="service-item">
      <div class="service-icon" role="img" aria-label="Hair dryer icon"></div>
      <div class="service-info"><p class="service-name">Blow Waves</p><p class="service-meta">30 min<span class="sep">|</span>50 $</p></div>
      <svg class="checkbox" viewBox="0 0 56 56"><rect x="4" y="4" width="48" height="48" fill="none" stroke="#38ace4" stroke-width="4"/><path d="M14 28l10 10 24-26" fill="none" stroke="#38ace4" stroke-width="6" stroke-linecap="round" stroke-linejoin="round"/></svg>
    </li>
    <li class="service-item">
      <div class="service-icon" role="img" aria-label="Hair wash treatment icon"></div>
      <div class="service-info"><p class="service-name">Hair Tratment</p><p class="service-meta">30 min<span class="sep">|</span>34 $</p></div>
      <svg class="checkbox" viewBox="0 0 56 56"><rect x="4" y="4" width="48" height="48" fill="none" stroke="#38ace4" stroke-width="4"/></svg>
    </li>
    <li class="service-item">
      <div class="service-icon" role="img" aria-label="Long hair extensions icon"></div>
      <div class="service-info"><p class="service-name">Hair Extensions</p><p class="service-meta">60 min<span class="sep">|</span>100 $</p></div>
      <svg class="checkbox" viewBox="0 0 56 56"><rect x="4" y="4" width="48" height="48" fill="none" stroke="#38ace4" stroke-width="4"/></svg>
    </li>
    <li class="service-item">
      <div class="service-icon" role="img" aria-label="Massage icon"></div>
      <div class="service-info"><p class="service-name">Massage</p><p class="service-meta">30 min<span class="sep">|</span>200 $</p></div>
      <svg class="checkbox" viewBox="0 0 56 56"><rect x="4" y="4" width="48" height="48" fill="none" stroke="#38ace4" stroke-width="4"/></svg>
    </li>
    <li class="service-item">
      <div class="service-icon" role="img" aria-label="Ear piercing icon"></div>
      <div class="service-info"><p class="service-name">Body Piercing</p><p class="service-meta">90 min<span class="sep">|</span>250 $</p></div>
      <svg class="checkbox" viewBox="0 0 56 56"><rect x="4" y="4" width="48" height="48" fill="none" stroke="#38ace4" stroke-width="4"/></svg>
    </li>
  </ul>
</div>
</body>
</html>
```